Q-Rolls Business Card

We are a modern retail clothing store. Established in 1994. I need a presentable card that will amaze vendors when given to them.

Front: Logo in middle
Info Side:

Name: Tomas Velder
Cell: 630-812-4463
Work: 630-917-3384 EXT. 417
Email: Tomas@q-rolls-example.com
Website: www.Q-rolls-example.com

Industry/Entity Type

Business

```html
<!DOCTYPE html>
<html lang="en">
<head>
<meta charset="utf-8">
<title>Q-Rolls Business Card</title>
<link href="https://fonts.googleapis.com/css2?family=Open+Sans:wght@400;600;700&display=swap" rel="stylesheet">
<style>
  :root {
    --backdrop: #2b2b2b;
    --card: #050505;
    --ink: #ffffff;
    --ink-soft: #e6e6e6;
  }
  * { margin: 0; padding: 0; box-sizing: border-box; }
  html, body { width: 1200px; height: 900px; overflow: hidden; }
  body {
    background: var(--backdrop);
    font-family: "Open Sans", Arial, sans-serif;
    position: relative;
  }
  .card {
    position: absolute;
    width: 665px;
    height: 380px;
    background: var(--card);
    border-radius: 22px;
    box-shadow: 0 14px 30px rgba(0,0,0,.45);
    color: var(--ink);
    overflow: hidden;
  }
  .card--front { left: 150px; top: 50px; }
  .card--info { left: 385px; top: 470px; }

  .wordmark {
    font-family: "Open Sans", Arial, sans-serif;
    font-weight: 700;
    text-transform: uppercase;
    color: var(--ink);
    letter-spacing: 2px;
    line-height: 1;
    white-space: nowrap;
  }
  .card--front .brand {
    position: absolute;
    left: 0; right: 0; top: 130px;
    text-align: center;
  }
  .card--front .wordmark { font-size: 78px; }
  .card--front .site {
    margin-top: 16px;
    font-size: 14px;
    font-weight: 600;
    letter-spacing: .5px;
  }

  .card--info .brand {
    position: absolute;
    right: 38px; top: 52px;
    text-align: right;
  }
  .card--info .wordmark { font-size: 62px; }
  .card--info .tagline {
    margin-top: 8px;
    font-size: 17px;
    letter-spacing: .6px;
  }
  .divider { position: absolute; left: 0; top: 0; }

  .contact {
    position: absolute;
    left: 40px; bottom: 34px;
  }
  .contact__name {
    font-size: 24px;
    font-weight: 700;
    text-transform: uppercase;
    letter-spacing: .5px;
    margin-bottom: 8px;
  }
  .contact__list { list-style: none; }
  .contact__item {
    display: flex;
    align-items: center;
    gap: 12px;
    font-size: 15px;
    color: var(--ink-soft);
    line-height: 21px;
  }
  .contact__item svg { width: 12px; height: 12px; flex: none; }
</style>
</head>
<body>

<section class="card card--front">
  <div class="brand">
    <div class="wordmark">Q-Rolls</div>
    <div class="site">www.q-rolls-example.com</div>
  </div>
</section>

<section class="card card--info">
  <svg class="divider" width="665" height="380" viewBox="0 0 665 380">
    <line x1="225" y1="238" x2="628" y2="160" stroke="#ffffff" stroke-width="2"/>
  </svg>
  <div class="brand">
    <div class="wordmark">Q-Rolls</div>
    <div class="tagline">Established in 1994</div>
  </div>
  <div class="contact">
    <div class="contact__name">Tomas Velder</div>
    <ul class="contact__list">
      <li class="contact__item">
        <svg viewBox="0 0 12 12"><rect x="3" y="0.5" width="6" height="11" rx="1" fill="none" stroke="#fff" stroke-width="1.2"/><circle cx="6" cy="9.5" r=".8" fill="#fff"/></svg>
        630-812-4463
      </li>
      <li class="contact__item">
        <svg viewBox="0 0 12 12"><path d="M2.5 1 L4.5 1 L5.2 3.6 L4 4.6 Q5 7 7.4 8 L8.4 6.8 L11 7.5 L11 9.5 Q10.5 11 9 11 Q1 10 1 2.5 Q1 1 2.5 1 Z" fill="#fff"/></svg>
        630-917-3384 EXT. 417
      </li>
      <li class="contact__item">
        <svg viewBox="0 0 12 12"><rect x=".7" y="2" width="10.6" height="8" fill="none" stroke="#fff" stroke-width="1.2"/><path d="M1 2.5 L6 6.5 L11 2.5" fill="none" stroke="#fff" stroke-width="1.2"/></svg>
        Tomas@q-rolls-example.com
      </li>
      <li class="contact__item">
        <svg viewBox="0 0 12 12"><circle cx="6" cy="6" r="5.2" fill="none" stroke="#fff" stroke-width="1.1"/><ellipse cx="6" cy="6" rx="2.2" ry="5.2" fill="none" stroke="#fff" stroke-width="1"/><line x1="1" y1="6" x2="11" y2="6" stroke="#fff" stroke-width="1"/></svg>
        www.Q-rolls-example.com
      </li>
    </ul>
  </div>
</section>

</body>
</html>
```